Window cleaning company in need of leaflet design

Family run business requires leaflet design.
Our company uses water fed pole with pure water which is what the leaflet needs to emphasise on (include a background picture of a water fed pole cleaning a window.)

other services we offer which i would like to include are:
• facia/soffit cleaning.
• Conservatory cleans.
• Gutter clearing which is performed by a gutter vacuum pictures of gutters before and after clean are provided to every customer if they require.
• pressure washing

uploaded company logo to be included on leaflet.
number to include is 07715264389
email address is Rtglasscare@mailbay.test
would also like a facebook symbol included to show we are on social media.
Thank you

Font styles to use
Serif
Sans Serif

Colors
00a990
33a6d7
3276b5
3277b5
34a7d8
87cfc6
33b8a4
cfdfed
85acd3

Requirements
Must have
• We use traditional and water fed pole methods of cleaning. So those hard to reach or awkward to clean windows are not a problem. No need for ladders.

Our water fed pole system uses 100% pure water. This is water that has been de-ironised and de-mineralised to ensue it’s perfectly pure for a spot free finish.

• fully insured

• regular and reliable service
• one off cleans available

Call dean on 07715264389 for a free quote

```html
<!DOCTYPE html>
<html lang="en">
<head>
<meta charset="utf-8">
<title>R.T Glass Care – Leaflet</title>
<link rel="stylesheet" href="https://fonts.googleapis.com/css2?family=Poppins:wght@400;500;600;700&display=swap">
<style>
  :root {
    --stage: #000000;
    --paper: #ffffff;
    --navy: #1f3f7a;
    --blue: #3276b5;
    --sky: #34a7d8;
    --teal: #00a990;
    --teal-soft: #33b8a4;
    --mint: #87cfc6;
    --mist: #cfdfed;
    --steel: #85acd3;
  }
  * { box-sizing: border-box; margin: 0; padding: 0; }
  html, body { width: 1200px; height: 1200px; overflow: hidden; background: var(--stage); }
  body { font-family: "Poppins", sans-serif; position: relative; }

  .leaflet {
    position: absolute; left: 204px; top: 88px; width: 792px; height: 1025px;
    background: var(--paper); overflow: hidden;
  }

  /* header */
  .brand {
    position: absolute; left: 66px; top: 46px;
    font-weight: 500; font-size: 26px; color: var(--navy); letter-spacing: 0.2px;
  }
  .contact-band { position: absolute; left: 378px; top: 14px; width: 414px; height: 72px; }
  .contact-list { position: absolute; left: 458px; top: 22px; list-style: none; }
  .contact-list li {
    display: flex; align-items: center; gap: 10px;
    color: #fff; font-size: 17.5px; height: 27px;
  }
  .contact-icon { width: 20px; height: 20px; }

  /* hero photo */
  .hero-photo {
    position: absolute; left: 0; top: 102px; width: 792px; height: 354px;
    background: linear-gradient(160deg, #6f8fc4 0%, #a9bee0 35%, #4d6e9e 60%, #2f5a63 80%, #8fa4c9 100%);
  }

  /* intro */
  .water-photo {
    position: absolute; left: 520px; top: 470px; width: 272px; height: 498px;
    background: linear-gradient(180deg, #8fb6cf 0%, #b7d3e0 40%, #a4c6d6 70%, #c8dde8 100%);
  }
  .intro-shape { position: absolute; left: 0; top: 470px; width: 792px; height: 201px; }
  .intro-text {
    position: absolute; left: 25px; top: 490px; width: 530px;
    color: #fff; font-size: 15.6px; line-height: 21px;
  }
  .intro-text p + p { margin-top: 10px; }
  .intro-text strong { font-weight: 700; }

  /* services */
  .services-bg { position: absolute; left: 0; top: 671px; width: 792px; height: 300px; }
  .services-tab { position: absolute; left: 0; top: 677px; width: 305px; height: 52px; }
  .services-title {
    position: absolute; left: 22px; top: 683px;
    display: flex; align-items: center; gap: 12px;
    font-size: 29px; font-weight: 500; color: var(--teal); letter-spacing: 0.3px;
  }
  .services-list {
    position: absolute; left: 22px; top: 754px; width: 390px; list-style: none;
    font-size: 17px; line-height: 23.4px; color: var(--blue);
  }
  .services-list li { display: flex; gap: 7px; }
  .services-list .name { font-weight: 700; }
  .services-list .detail { display: block; font-weight: 400; }
  .tick { flex: 0 0 18px; width: 18px; height: 18px; margin-top: 3px; }

  .feature { position: absolute; height: 80px; right: 0; display: flex; align-items: center; }
  .feature-bar {
    position: absolute; left: 36px; right: 0; top: 17px; height: 48px;
    background: linear-gradient(90deg, var(--teal-soft) 0%, #4cc2ad 60%, rgba(135,207,198,0.75) 100%);
  }
  .feature-badge { position: relative; width: 82px; height: 82px; flex: 0 0 82px; }
  .feature-label {
    position: relative; margin-left: 16px; color: #fff; font-size: 18px; font-weight: 500;
  }
  .feature--regular { left: 375px; top: 687px; }
  .feature--oneoff { left: 417px; top: 780px; }
  .feature--insured { left: 468px; top: 873px; }

  /* footer */
  .footer-rule { position: absolute; left: 0; top: 969px; width: 792px; height: 5px; background: var(--blue); }
  .cta {
    position: absolute; left: 22px; top: 986px;
    display: flex; align-items: center; gap: 12px;
    font-size: 21.5px; font-weight: 500; color: var(--blue);
  }
  .cta b { font-weight: 700; }
  .cta .hl { color: var(--teal-soft); font-weight: 700; }
  .social-mark {
    position: absolute; left: 739px; top: 986px; width: 31px; height: 31px;
    background: var(--blue); border-radius: 2px;
  }
</style>
</head>
<body>
<main class="leaflet">

  <header>
    <div class="brand">R.T Glass Care</div>
    <svg class="contact-band" viewBox="0 0 414 72" aria-hidden="true">
      <polygon points="22,0 34,0 12,72 0,72" fill="var(--sky)"/>
      <polygon points="48,0 414,0 414,72 26,72" fill="var(--blue)"/>
    </svg>
    <ul class="contact-list">
      <li>
        <svg class="contact-icon" viewBox="0 0 20 20" aria-hidden="true">
          <circle cx="10" cy="10" r="10" fill="var(--teal-soft)"/>
          <path d="M7 5.2l1.6 2.3-1 1.1c.6 1.4 1.7 2.5 3.1 3.1l1.1-1 2.3 1.6-.8 1.9c-3.8-.2-6.9-3.3-7.1-7.1z" fill="#fff"/>
        </svg>
        07715264389
      </li>
      <li>
        <svg class="contact-icon" viewBox="0 0 20 20" aria-hidden="true">
          <circle cx="10" cy="10" r="10" fill="var(--teal-soft)"/>
          <rect x="5" y="6.5" width="10" height="7" rx="1" fill="none" stroke="#fff" stroke-width="1.3"/>
          <path d="M5.3 7l4.7 3.6L14.7 7" fill="none" stroke="#fff" stroke-width="1.3"/>
        </svg>
        Rtglasscare@mailbay.test
      </li>
    </ul>
  </header>

  <div class="hero-photo" role="img" aria-label="Photo of a water fed pole brush cleaning a conservatory glass roof against a blue sky"></div>

  <section class="intro">
    <div class="water-photo" role="img" aria-label="Close-up photo of water droplets running down a window pane"></div>
    <svg class="intro-shape" viewBox="0 0 792 201" aria-hidden="true">
      <polygon points="0,0 576,0 658,201 0,201" fill="var(--blue)"/>
      <polygon points="580,0 590,0 674,201 664,201" fill="var(--sky)"/>
    </svg>
    <div class="intro-text">
      <p><strong>R.T GLASS CARE</strong> is a family business using traditional and water fed pole methods of cleaning. So those hard to reach or awkward to clean windows are not a problem. No need for ladders.</p>
      <p>Our water fed pole system uses 100% pure water. This is water that has been de-ironised and de-mineralised to ensue it's perfectly pure for a spot free finish.</p>
    </div>
  </section>

  <section class="services">
    <svg class="services-bg" viewBox="0 0 792 300" aria-hidden="true">
      <polygon points="0,0 372,0 470,300 0,300" fill="var(--mist)"/>
    </svg>
    <svg class="services-tab" viewBox="0 0 305 52" aria-hidden="true">
      <polygon points="0,0 305,0 280,52 0,52" fill="#fff"/>
    </svg>
    <h2 class="services-title">
      <svg width="11" height="18" viewBox="0 0 11 18" aria-hidden="true"><polygon points="0,0 11,9 0,18" fill="var(--blue)"/></svg>
      OUR SERVICES
    </h2>
    <ul class="services-list">
      <li>
        <svg class="tick" viewBox="0 0 18 18" aria-hidden="true"><rect x="1" y="3" width="14" height="14" fill="none" stroke="var(--teal-soft)" stroke-width="1.6"/><path d="M4 9l4 4 9-11" fill="none" stroke="var(--teal-soft)" stroke-width="2.4"/></svg>
        <span class="name">FACIA / SOFFIT CLEANING</span>
      </li>
      <li>
        <svg class="tick" viewBox="0 0 18 18" aria-hidden="true"><rect x="1" y="3" width="14" height="14" fill="none" stroke="var(--teal-soft)" stroke-width="1.6"/><path d="M4 9l4 4 9-11" fill="none" stroke="var(--teal-soft)" stroke-width="2.4"/></svg>
        <span class="name">CONSERVATORY CLEANS</span>
      </li>
      <li>
        <svg class="tick" viewBox="0 0 18 18" aria-hidden="true"><rect x="1" y="3" width="14" height="14" fill="none" stroke="var(--teal-soft)" stroke-width="1.6"/><path d="M4 9l4 4 9-11" fill="none" stroke="var(--teal-soft)" stroke-width="2.4"/></svg>
        <span><span class="name">GUTTER CLEARING</span>
        <span class="detail">which is performed by a gutter vacuum pictures of gutters before and after clean are provided to every customer if they require.</span></span>
      </li>
      <li>
        <svg class="tick" viewBox="0 0 18 18" aria-hidden="true"><rect x="1" y="3" width="14" height="14" fill="none" stroke="var(--teal-soft)" stroke-width="1.6"/><path d="M4 9l4 4 9-11" fill="none" stroke="var(--teal-soft)" stroke-width="2.4"/></svg>
        <span class="name">PRESSURE WASHING</span>
      </li>
    </ul>

    <div class="feature feature--regular">
      <div class="feature-bar"></div>
      <svg class="feature-badge" viewBox="0 0 82 82" aria-hidden="true">
        <circle cx="41" cy="41" r="40" fill="#fff"/>
        <circle cx="41" cy="41" r="34" fill="none" stroke="var(--blue)" stroke-width="3"/>
        <rect x="25" y="26" width="30" height="28" rx="3" fill="none" stroke="var(--blue)" stroke-width="3"/>
        <rect x="25" y="26" width="30" height="7" fill="var(--blue)"/>
        <line x1="31" y1="22" x2="31" y2="29" stroke="var(--blue)" stroke-width="3"/>
        <line x1="49" y1="22" x2="49" y2="29" stroke="var(--blue)" stroke-width="3"/>
        <g fill="var(--blue)"><rect x="29" y="37" width="4" height="4"/><rect x="36" y="37" width="4" height="4"/><rect x="43" y="37" width="4" height="4"/><rect x="29" y="44" width="4" height="4"/><rect x="36" y="44" width="4" height="4"/></g>
        <circle cx="53" cy="52" r="7" fill="var(--sky)" stroke="#fff" stroke-width="2"/>
        <path d="M49.5 52l2.5 2.5 4.5-5" fill="none" stroke="#fff" stroke-width="2"/>
      </svg>
      <span class="feature-label">REGULAR &amp; RELIABLE SERVICE</span>
    </div>

    <div class="feature feature--oneoff">
      <div class="feature-bar"></div>
      <svg class="feature-badge" viewBox="0 0 82 82" aria-hidden="true">
        <circle cx="41" cy="41" r="40" fill="#fff"/>
        <circle cx="41" cy="41" r="34" fill="none" stroke="var(--blue)" stroke-width="3"/>
        <path d="M46 30q1 9 10 10q-9 1-10 10q-1-9-10-10q9-1 10-10z" fill="none" stroke="var(--blue)" stroke-width="2.2" stroke-linejoin="round"/>
        <path d="M32 22q.6 5 5 5.5q-4.4.5-5 5.5q-.6-5-5-5.5q4.4-.5 5-5.5z" fill="none" stroke="var(--blue)" stroke-width="2" stroke-linejoin="round"/>
        <path d="M31 45q.6 5 5 5.5q-4.4.5-5 5.5q-.6-5-5-5.5q4.4-.5 5-5.5z" fill="none" stroke="var(--blue)" stroke-width="2" stroke-linejoin="round"/>
      </svg>
      <span class="feature-label">ONE OFF CLEANS AVAILABLE</span>
    </div>

    <div class="feature feature--insured">
      <div class="feature-bar"></div>
      <svg class="feature-badge" viewBox="0 0 82 82" aria-hidden="true">
        <circle cx="41" cy="41" r="40" fill="#fff"/>
        <circle cx="41" cy="41" r="34" fill="none" stroke="var(--blue)" stroke-width="3"/>
        <path d="M41 20l16 6v11c0 11-7 19-16 23c-9-4-16-12-16-23V26z" fill="none" stroke="var(--blue)" stroke-width="3" stroke-linejoin="round"/>
        <path d="M41 25l11 4v8c0 8-5 14-11 17c-6-3-11-9-11-17v-8z" fill="var(--steel)" opacity="0.45"/>
        <path d="M34 40l5 5 9-10" fill="none" stroke="var(--blue)" stroke-width="3.2" stroke-linecap="round" stroke-linejoin="round"/>
      </svg>
      <span class="feature-label">FULLY INSURED</span>
    </div>
  </section>

  <footer>
    <div class="footer-rule"></div>
    <p class="cta">
      <svg width="11" height="18" viewBox="0 0 11 18" aria-hidden="true"><polygon points="0,0 11,9 0,18" fill="var(--blue)"/></svg>
      <span>CALL <b>DEAN</b> ON <span class="hl">07715264389</span> FOR A <span class="hl">FREE QUOTE</span>!</span>
    </p>
    <div class="social-mark" aria-label="Find us on social media"></div>
  </footer>

</main>
</body>
</html>
```